Luxury Wine Label for New Startup Winery

We need a wine label for our new winery startup. We have worked with a local designer but do not feel the resulting label / logo have the elevation required to present our brand as a luxury wine. Our winery is called "Halvorsen Cellars" and we are focused on extremely high quality hand crafted artisan and estate wines from the Pacific Northwest.
We would like to see designs that utilize a tree line, or other imagery that represents the "Halvorsen" part of our company name. Another interesting feature could be wood grain.
A logo will be required based on your design so please design with this in mind:
This logo should be consistent with the wine bottle label design, and should be representative of our high end exclusive wine while giving a sense of place (Oregon/ Pacific Northwest.)
I will supply an image of the design we received from our local designer, PLEASE NOTE: in general we do like wood grain and tree line concepts but feel the execution was poorly done.
ATTN: Logo design should be suitable for use on: Bottles (Red wine/rose/white wine), Bussiness cards, vehicle signage, business signage, etc
P.S.:
If you have a design that is not outside the box we are still interested in seeing it.
Label is for a burgundy style bottle with a label height of 3.5 - 4" and a width of 3.5-4"
any label <= 4"x4" and >=3.5"x3.5" will be acceptable:
HOWEVER Width should be greater than or equal to height due to the bottle format
Target Market(s)
Wine enthusiasts with adequate discretionary budgets to afford $100 bottles of wine.
Industry/Entity Type
Wine / Winery
Requirements
Must have
- A sense of luxury, a feel of exclusivity, and a theme consistent with our product and brand name
Nice to have
- Tree line, wood grain or other wood themes. Serif fonts
Should not have
- anything cheesy, off topic, hard to read script fonts or anything that makes the label hard to read from a few feet away or too busy

```html
<!DOCTYPE html>
<html lang="en">
<head>
<meta charset="utf-8">
<title>Halvorsen Cellars – Label Series</title>
<link rel="stylesheet" href="https://fonts.googleapis.com/css2?family=Montserrat:wght@800&family=Marcellus&family=Libre+Caslon+Text&display=swap">
<style>
  :root {
    --paper: #ffffff;
    --wine: #5a1526;
    --wine-deep: #3f0c18;
    --wine-light: #6a1d2f;
    --gold: #e9c15a;
    --gold-soft: #f2d683;
    --gold-dark: #b98a2c;
    --ornament: #9a6a34;
    --cream: #ebe4d6;
    --ink: #3b1018;
    --rose: #b4267f;
    --white-wine: #d23c27;
    --black: #050505;
  }
  * { margin: 0; padding: 0; box-sizing: border-box; }
  html, body { width: 848px; height: 1200px; overflow: hidden; background: var(--paper); }
  .sheet { position: relative; width: 848px; height: 1200px; }

  .label { position: absolute; left: 42px; width: 408px; height: 356px; overflow: hidden; background: var(--wine); }
  .label--syrah { top: 40px; }
  .label--rose { top: 413px; }
  .label--white { top: 795px; }

  .label__grain {
    position: absolute; inset: 0;
    background:
      radial-gradient(ellipse 60px 110px at 20% 35%, var(--wine-light) 0%, transparent 70%),
      radial-gradient(ellipse 50px 90px at 82% 25%, var(--wine-light) 0%, transparent 70%),
      radial-gradient(ellipse 70px 60px at 65% 70%, var(--wine-light) 0%, transparent 70%),
      linear-gradient(90deg, var(--wine) 0%, #561323 50%, var(--wine) 100%);
  }

  .label__ornament-top {
    position: absolute; left: 0; top: 0; width: 100%; height: 10px;
    background: linear-gradient(180deg, var(--gold-soft) 0 3px, var(--gold) 3px, var(--ornament) 100%);
  }

  .label__mark {
    position: absolute; left: 174px; top: 62px; width: 60px; height: 60px;
    border-radius: 50%; background: var(--gold);
  }

  .wordmark {
    position: absolute; left: 54px; top: 163px; width: 300px;
    font-family: "Montserrat", sans-serif; font-weight: 800; color: var(--gold); line-height: 1;
  }
  .wordmark__name { display: block; font-size: 40px; letter-spacing: 0.3px; text-align: center; }
  .wordmark__sub { display: block; font-size: 16px; letter-spacing: 4px; text-align: right; margin-top: 6px; }

  .label__band {
    position: absolute; left: 0; top: 254px; width: 100%; height: 59px;
    background: var(--cream); color: var(--ink); text-align: center;
    font-family: "Libre Caslon Text", serif;
  }
  .label__region { display: block; font-size: 14px; letter-spacing: 0.3px; margin-top: 12px; }
  .label__vintage { display: block; font-size: 13px; margin-top: 4px; }

  .label__ornament-bottom {
    position: absolute; left: 0; top: 313px; width: 100%; height: 43px;
    border-top: 3px solid var(--gold); border-bottom: 3px solid var(--gold);
    background: linear-gradient(180deg, var(--ornament) 0%, #c49a4a 50%, var(--ornament) 100%);
  }
  .label__varietal {
    position: absolute; left: 124px; top: 313px; width: 167px; height: 40px;
    display: flex; align-items: center; justify-content: center;
    font-family: "Marcellus", serif; font-size: 29px; letter-spacing: 1px; color: var(--gold);
    background: var(--wine-deep);
  }
  .label--rose .label__varietal { background: var(--rose); }
  .label--white .label__varietal { background: var(--white-wine); }

  .logo-plate {
    position: absolute; left: 488px; top: 141px; width: 299px; height: 120px;
    background: var(--black); color: #ffffff;
    font-family: "Montserrat", sans-serif; font-weight: 800;
    display: flex; flex-direction: column; justify-content: center; padding-left: 22px;
  }
  .logo-plate__name { font-size: 34px; line-height: 1; letter-spacing: 0.3px; }
  .logo-plate__sub { font-size: 14px; letter-spacing: 4px; margin-top: 6px; text-align: right; padding-right: 36px; }

  .scene-badge {
    position: absolute; left: 490px; top: 785px; width: 194px; height: 194px; border-radius: 50%;
    background: linear-gradient(180deg, var(--gold-soft) 0%, var(--gold) 40%, #8a4a34 58%, var(--wine) 70%, var(--wine-deep) 100%);
  }
</style>
</head>
<body>
<main class="sheet">

  <section class="label label--syrah">
    <div class="label__grain" role="img" aria-label="Burgundy wood grain texture"></div>
    <div class="label__ornament-top" role="img" aria-label="Gold ornamental border"></div>
    <div class="label__mark"></div>
    <div class="wordmark"><span class="wordmark__name">HALVORSEN</span><span class="wordmark__sub">CELLARS</span></div>
    <div class="label__band"><span class="label__region">WILLAMETTE VALLEY</span><span class="label__vintage">-2024-</span></div>
    <div class="label__ornament-bottom" role="img" aria-label="Gold and burgundy ornamental border pattern"></div>
    <div class="label__varietal">SYRAH</div>
  </section>

  <section class="label label--rose">
    <div class="label__grain" role="img" aria-label="Burgundy wood grain texture"></div>
    <div class="label__ornament-top" role="img" aria-label="Gold ornamental border"></div>
    <div class="label__mark"></div>
    <div class="wordmark"><span class="wordmark__name">HALVORSEN</span><span class="wordmark__sub">CELLARS</span></div>
    <div class="label__band"><span class="label__region">WILLAMETTE VALLEY</span><span class="label__vintage">-2024-</span></div>
    <div class="label__ornament-bottom" role="img" aria-label="Gold and burgundy ornamental border pattern"></div>
    <div class="label__varietal">ROSE</div>
  </section>

  <section class="label label--white">
    <div class="label__grain" role="img" aria-label="Burgundy wood grain texture"></div>
    <div class="label__ornament-top" role="img" aria-label="Gold ornamental border"></div>
    <div class="label__mark"></div>
    <div class="wordmark"><span class="wordmark__name">HALVORSEN</span><span class="wordmark__sub">CELLARS</span></div>
    <div class="label__band"><span class="label__region">WILLAMETTE VALLEY</span><span class="label__vintage">-2024-</span></div>
    <div class="label__ornament-bottom" role="img" aria-label="Gold and burgundy ornamental border pattern"></div>
    <div class="label__varietal">WHITE</div>
  </section>

  <div class="logo-plate">
    <span class="logo-plate__name">HALVORSEN</span>
    <span class="logo-plate__sub">CELLARS</span>
  </div>

  <div class="scene-badge" role="img" aria-label="Round badge with mountains, fir tree line and lake in gold and burgundy"></div>

</main>
</body>
</html>
```